Simple Packaging Design For Camera Company

We need packaging designed for our product. Our product is a lens that fits onto smart phones, allowing better quality photos. We would like the design to be simple. Maybe the front cover with just the Lumora logo and the product name (CLEAR FIELD MAX) underneath. the box color a light grey and text black. instead of having a picture of our product we were thinking of a outline sketch of it.

Target Market(s)

anyone looking to take better photos, but not wanting a DSLR

Industry/Entity Type

Digital Camera

Font styles to use
Sans Serif

Requirements
Nice to have
• - A sketch outline of the product. not too detailed
• - Light grey background and black text
Should not have
• stock images

```html
<!DOCTYPE html>
<html lang="en">
<head>
<meta charset="utf-8">
<title>Lumora Clear Field MAX – Box Front and Side</title>
<link rel="stylesheet" href="https://fonts.googleapis.com/css2?family=Montserrat:wght@500&family=Barlow+Condensed:wght@500;600&display=swap">
<style>
  :root {
    --page-bg: #efedee;
    --panel-grey: #dcdcdc;
    --panel-grey-light: #e8e8e8;
    --ink: #2a2a2a;
    --rule: #555555;
    --photo-light: #cfcfcf;
    --photo-dark: #8f8f8f;
  }
  html, body {
    margin: 0;
    width: 1200px;
    height: 900px;
    overflow: hidden;
    background: var(--page-bg);
  }
  .canvas {
    position: relative;
    width: 1200px;
    height: 900px;
  }
  .box-face {
    position: absolute;
    top: 170px;
    height: 560px;
    background: linear-gradient(160deg, var(--panel-grey-light), var(--panel-grey));
    box-shadow: 0 2px 6px rgba(0,0,0,0.08);
    overflow: hidden;
  }
  .front-panel { left: 280px; width: 460px; }
  .side-panel  { left: 740px; width: 180px; border-left: 1px solid #c9c9c9; }

  .fold-line {
    position: absolute;
    inset: 0;
  }
  .title-block {
    position: absolute;
    left: 0;
    right: 0;
    top: 120px;
    text-align: center;
    font-family: "Montserrat", sans-serif;
    font-weight: 500;
    color: var(--ink);
  }
  .brand-name {
    margin: 0;
    font-size: 54px;
    font-weight: 500;
    letter-spacing: 6px;
    line-height: 1;
  }
  .product-name {
    margin: 14px 0 0;
    font-size: 18px;
    letter-spacing: 4px;
    line-height: 1;
  }
  .product-photo {
    position: absolute;
    left: 40px;
    top: 290px;
    width: 380px;
    height: 250px;
    background: radial-gradient(ellipse at 50% 55%, var(--photo-dark), var(--photo-light) 75%);
    border-radius: 4px;
  }

  .spec-list {
    position: absolute;
    left: 18px;
    right: 14px;
    top: 150px;
    margin: 0;
    padding: 0;
    font-family: "Barlow Condensed", sans-serif;
    color: var(--ink);
  }
  .spec-item {
    border-bottom: 1px solid var(--rule);
    padding: 6px 0 5px;
  }
  .spec-item:last-child { border-bottom: none; }
  .spec-label {
    font-weight: 600;
    font-size: 15px;
    display: block;
  }
  .spec-value {
    font-weight: 500;
    font-size: 12px;
    display: block;
    margin: 0;
    white-space: nowrap;
  }
</style>
</head>
<body>
<main class="canvas">
  <section class="box-face front-panel">
    <svg class="fold-line" width="460" height="560" viewBox="0 0 460 560" aria-hidden="true">
      <line x1="290" y1="18" x2="460" y2="118" stroke="#555" stroke-width="1.2" stroke-dasharray="6 5"/>
    </svg>
    <div class="title-block">
      <h1 class="brand-name">LUMORA</h1>
      <p class="product-name">CLEAR FIELD MAX</p>
    </div>
    <div class="product-photo" role="img" aria-label="Black and white photo of the phone lens kit, lens caps and cleaning cloth on a wooden table"></div>
  </section>

  <section class="box-face side-panel">
    <dl class="spec-list">
      <div class="spec-item"><dt class="spec-label">Material :</dt><dd class="spec-value">Multi-layer Optics + Alu</dd></div>
      <div class="spec-item"><dt class="spec-label">Lens Type :</dt><dd class="spec-value">Clear Field MAX</dd></div>
      <div class="spec-item"><dt class="spec-label">Magnification :</dt><dd class="spec-value">0.5X</dd></div>
      <div class="spec-item"><dt class="spec-label">FOV :</dt><dd class="spec-value">110 Degrees</dd></div>
      <div class="spec-item"><dt class="spec-label">Distortion :</dt><dd class="spec-value">0.5%</dd></div>
      <div class="spec-item"><dt class="spec-label">Compatible :</dt><dd class="spec-value">Most Mobile Phones &amp; Tablets</dd></div>
    </dl>
  </section>
</main>
</body>
</html>
```